Brochure for a new technology in mineral processing industry

We require a rush design for a brochure for an upcoming conference on 8th December. It needs to comply with our logo colours and web site (www.korvaleng.com.au). The attached is a mockup (not very creative) that should be used as a guide only. A word version is available upon request. The design should be aligned with a science and engineering based organisation and not be too busy in its design. Looking for classic but simple lines. Photos loaded up should be used at the designers discretion to enhance look.

Target Market(s)

Brochure to be used to market to mining industry.

Industry/Entity Type

Mining

Requirements
Must have
• The brochure must have simple lines - not to be busy. Colours to match logo and corporate colours and website branding.
Nice to have
• Themes that we feel would be nice to bring through:
• 1. Step Change/modern/innovation
• 2. Clever science being commercialised
• 3. Mining Industry
Should not have
• Not too busy. Arty perspectives.

```html
<!DOCTYPE html>
<html lang="en">
<head>
<meta charset="utf-8">
<title>Glycine Leaching Process – Korval Engineering</title>
<link href="https://fonts.googleapis.com/css2?family=Montserrat:wght@400;500;600;700;800&display=swap" rel="stylesheet">
<style>
  :root {
    --title-blue: #3b66ae;
    --ink: #3a3a3a;
    --band-dark: #a65a22;
    --band-light: #e9a35d;
    --rule: #c47b45;
    --ring: #2f6fb5;
    --green-a: #a9d8a2; --green-b: #6fbb6d;
    --blue-a: #a4d3f2; --blue-b: #5aaee3;
    --tan-a: #e2d8c6; --tan-b: #bba98c;
    --grey-a: #f2f2f2; --grey-b: #c9c9c9;
    --yellow-a: #fbf9b8; --yellow-b: #eee96a;
    --purple-a: #c7c7ec; --purple-b: #9a9ad2;
    --tile-edge: #8d8d8d;
  }
  * { box-sizing: border-box; margin: 0; padding: 0; }
  html, body { width: 848px; height: 1200px; overflow: hidden; background: #fff; }
  body { font-family: "Montserrat", Arial, sans-serif; color: var(--ink); }
  .page { position: relative; width: 848px; height: 1200px; }

  .title { position: absolute; left: 43px; top: 66px; font-size: 29px; font-weight: 500; color: var(--title-blue); }
  .intro { position: absolute; left: 43px; top: 118px; width: 770px; font-size: 16px; line-height: 21px; }
  .intro p { margin-bottom: 20px; }
  .intro strong, .outro strong { font-weight: 700; }

  .band {
    position: absolute; left: 34px; top: 305px; width: 789px; height: 49px;
    background: linear-gradient(to bottom, var(--band-dark), var(--band-light) 50%, var(--band-dark));
    color: #fff; text-align: center; font-weight: 700; font-size: 14px; line-height: 18px; padding-top: 6px; letter-spacing: .3px;
  }

  .table { position: absolute; left: 50px; top: 381px; width: 770px; height: 230px; }
  .tile {
    position: absolute; width: 70px; height: 70px; border-radius: 9px; border: 1px solid var(--tile-edge);
    text-align: center; color: #222;
  }
  .tile .num { display: block; font-size: 8px; margin-top: 3px; color: #444; }
  .tile .sym { display: block; font-size: 28px; font-weight: 800; line-height: 28px; }
  .tile .name, .tile .mass { display: block; font-size: 8px; line-height: 9px; color: #444; }
  .green  { background: linear-gradient(var(--green-a), var(--green-b)); }
  .blue   { background: linear-gradient(var(--blue-a), var(--blue-b)); }
  .tan    { background: linear-gradient(var(--tan-a), var(--tan-b)); }
  .grey   { background: linear-gradient(var(--grey-a), var(--grey-b)); }
  .yellow { background: linear-gradient(var(--yellow-a), var(--yellow-b)); }
  .purple { background: linear-gradient(var(--purple-a), var(--purple-b)); }

  .legend { position: absolute; left: 50px; top: 633px; width: 770px; height: 80px; }
  .key {
    position: absolute; top: 0; width: 114px; height: 80px; border-radius: 6px; border: 1px solid var(--tile-edge);
    display: flex; align-items: center; justify-content: center; text-align: center;
    font-size: 10px; font-weight: 700; line-height: 12px; color: #222;
  }

  .divider { position: absolute; top: 768px; height: 3px; background: var(--rule); }
  .divider.left { left: 36px; width: 316px; }
  .divider.right { left: 498px; width: 316px; }
  .brand { position: absolute; left: 352px; top: 756px; width: 146px; text-align: center; font-size: 14px; font-weight: 700; color: var(--band-dark); line-height: 26px; }
  .brand .mark { display: inline-block; width: 12px; height: 12px; background: var(--band-dark); margin-right: 6px; vertical-align: -1px; }

  .outro { position: absolute; left: 43px; top: 826px; width: 770px; font-size: 16px; line-height: 21px; }
  .outro p { margin-bottom: 20px; }

  .photo {
    position: absolute; top: 1005px; width: 152px; height: 152px; border-radius: 50%;
    border: 3px solid var(--ring); box-shadow: inset 0 0 0 6px #fff;
  }
  .photo.metal { left: 73px; background: radial-gradient(circle at 45% 50%, #c9c9c9, #6f6f6f 60%, #fff 61%); }
  .photo.ore-green { left: 350px; background: radial-gradient(circle, #4f8a86, #3b4d6a 55%, #8a6a3a 70%, #fff 71%); }
  .photo.ore-blue { left: 627px; background: radial-gradient(circle, #6a4f8f, #2f3f7a 55%, #8a4a5a 70%, #fff 71%); }
</style>
</head>
<body>
<div class="page">
  <h1 class="title">Glycine Leaching Process</h1>
  <div class="intro">
    <p>The Glycine Leaching Process is an environmentally benign hydrometallurgical process that will leach base and precious metal oxide, mixed oxide and sulphide ores.</p>
    <p>Glycine is the simplest and cheapest amino acid, and is available in bulk in different grades. <strong>It is an environmentally safe and stable reagent</strong> and is biodegradable and easily metabolized in most living organisms.</p>
    <p><strong>It is selective on which metals it leaches and does not leach common gangue minerals.</strong></p>
  </div>

  <div class="band">Leaching characteristics of metals under consideration at<br>pH values between 9 and 12 with Sodium Glycinate as solvent</div>

  <div class="table">
    <div class="tile blue" style="left:0;top:0"><span class="num">25</span><span class="sym">Mn</span><span class="name">Manganese</span><span class="mass">54.9</span></div>
    <div class="tile blue" style="left:77px;top:0"><span class="num">26</span><span class="sym">Fe</span><span class="name">Iron</span><span class="mass">55.9</span></div>
    <div class="tile tan" style="left:154px;top:0"><span class="num">27</span><span class="sym">Co</span><span class="name">Colbalt</span><span class="mass">58.9</span></div>
    <div class="tile tan" style="left:231px;top:0"><span class="num">28</span><span class="sym">Ni</span><span class="name">Nickel</span><span class="mass">58.7</span></div>
    <div class="tile tan" style="left:308px;top:0"><span class="num">29</span><span class="sym">Cu</span><span class="name">Copper</span><span class="mass">63.5</span></div>
    <div class="tile grey" style="left:385px;top:0"><span class="num">30</span><span class="sym">Zn</span><span class="name">Zinc</span><span class="mass">65.4</span></div>
    <div class="tile green" style="left:462px;top:0"><span class="num">31</span><span class="sym">Ga</span><span class="name">Gallium</span><span class="mass">69.7</span></div>
    <div class="tile green" style="left:539px;top:0"><span class="num">32</span><span class="sym">Ge</span><span class="name">Germanium</span><span class="mass">72.6</span></div>
    <div class="tile purple" style="left:616px;top:0"><span class="num">33</span><span class="sym">As</span><span class="name">Arsenic</span><span class="mass">74.9</span></div>
    <div class="tile purple" style="left:693px;top:0"><span class="num">34</span><span class="sym">Se</span><span class="name">Selenium</span><span class="mass">79.0</span></div>

    <div class="tile green" style="left:77px;top:77px"><span class="num">44</span><span class="sym">Ru</span><span class="name">Ruthenium</span><span class="mass">101.0</span></div>
    <div class="tile green" style="left:154px;top:77px"><span class="num">45</span><span class="sym">Rh</span><span class="name">Rhodium</span><span class="mass">102.9</span></div>
    <div class="tile yellow" style="left:231px;top:77px"><span class="num">46</span><span class="sym">Pd</span><span class="name">Palladium</span><span class="mass">106.4</span></div>
    <div class="tile tan" style="left:308px;top:77px"><span class="num">47</span><span class="sym">Ag</span><span class="name">Silver</span><span class="mass">107.9</span></div>
    <div class="tile grey" style="left:385px;top:77px"><span class="num">48</span><span class="sym">Cd</span><span class="name">Cadmium</span><span class="mass">112.4</span></div>
    <div class="tile green" style="left:462px;top:77px"><span class="num">49</span><span class="sym">In</span><span class="name">Indium</span><span class="mass">114.8</span></div>
    <div class="tile green" style="left:539px;top:77px"><span class="num">50</span><span class="sym">Sn</span><span class="name">Tin</span><span class="mass">118.7</span></div>
    <div class="tile purple" style="left:616px;top:77px"><span class="num">51</span><span class="sym">Sb</span><span class="name">Antimony</span><span class="mass">121.8</span></div>
    <div class="tile purple" style="left:693px;top:77px"><span class="num">52</span><span class="sym">Te</span><span class="name">Tellurium</span><span class="mass">127.6</span></div>

    <div class="tile green" style="left:77px;top:154px"><span class="num">76</span><span class="sym">Os</span><span class="name">Osmium</span><span class="mass">190.2</span></div>
    <div class="tile green" style="left:154px;top:154px"><span class="num">77</span><span class="sym">Ir</span><span class="name">Iridium</span><span class="mass">192.2</span></div>
    <div class="tile yellow" style="left:231px;top:154px"><span class="num">78</span><span class="sym">Pt</span><span class="name">Platinum</span><span class="mass">195.1</span></div>
    <div class="tile tan" style="left:308px;top:154px"><span class="num">79</span><span class="sym">Au</span><span class="name">Gold</span><span class="mass">197.0</span></div>
    <div class="tile green" style="left:385px;top:154px"><span class="num">80</span><span class="sym">Hg</span><span class="name">Mercury</span><span class="mass">200.6</span></div>
    <div class="tile green" style="left:462px;top:154px"><span class="num">81</span><span class="sym">Tl</span><span class="name">Thallium</span><span class="mass">204.4</span></div>
    <div class="tile grey" style="left:539px;top:154px"><span class="num">82</span><span class="sym">Pb</span><span class="name">Lead</span><span class="mass">207.2</span></div>
    <div class="tile purple" style="left:616px;top:154px"><span class="num">83</span><span class="sym">Bi</span><span class="name">Bismuth</span><span class="mass">209.0</span></div>
  </div>

  <div class="legend">
    <div class="key green" style="left:0">Glycine<br>Solubility<br>Unknown</div>
    <div class="key blue" style="left:134px">Known<br>Clycine<br>Insoluble</div>
    <div class="key tan" style="left:268px">Known<br>Glycine<br>Leachable</div>
    <div class="key grey" style="left:402px">Known Glycine<br>Leachable Limited<br>Test work</div>
    <div class="key yellow" style="left:536px">Unknown<br>Subject to<br>Experiment</div>
    <div class="key purple" style="left:670px">Known<br>Amphoteric<br>Anions</div>
  </div>

  <div class="divider left"></div>
  <div class="brand"><span class="mark"></span>Korval Engineering</div>
  <div class="divider right"></div>

  <div class="outro">
    <p><strong>It is easily recovered and recycled.</strong> Flow sheet test work and modelling to date has shown that less than 5% Glycine loss can be expected. This means low reagent consumption costs for the major leaching reagent.</p>
    <p>It is a simple process than can be used with “off the shelf” items of equipment.</p>
    <p>Several applications of the technology are being developed.</p>
  </div>

  <div class="photo metal" role="img" aria-label="Close-up photo of a silvery metal nugget"></div>
  <div class="photo ore-green" role="img" aria-label="Macro photo of a mineral ore sample with green and gold crystals"></div>
  <div class="photo ore-blue" role="img" aria-label="Macro photo of a blue and purple sulphide ore sample"></div>
</div>
</body>
</html>
```